Flyer Design Project

Painting and Maintenance
This is what I have as idea as Job description
Refresh, renew & revive your home. from painting to carpentry. Do you guys have any epic unique slogan?
As what we do Residential - Commercial Interior - ExteriorTrim & Molding installationWainscoting - Wallpaper removalCabinet refinishing Woodwork EnamelingDeck & Fence Cleaning & SealingPressure washConcrete & Paver Washing
I would like to have a note that says-Prompt professional service-Free estimates-Insured -"visit us on ChatHive"
I would like new ideas from you guys as well!
Carpentry

```html
<!DOCTYPE html>
<html lang="en">
<head>
<meta charset="utf-8">
<title>Brindle Painting &amp; Maintenance – Postcard</title>
<link href="https://fonts.googleapis.com/css2?family=Oswald:wght@300;400;500;600&family=Open+Sans:wght@600;700&family=Arimo:wght@400;700&display=swap" rel="stylesheet">
<style>
  :root {
    --red: #c3272b;
    --red-dark: #9e1c20;
    --charcoal: #333335;
    --charcoal-light: #4a4a4c;
    --ink: #3a3a3c;
    --paper: #ffffff;
    --mist: #eeeeee;
    --stage: #e4e2df;
  }
  * { margin: 0; padding: 0; box-sizing: border-box; }
  html, body { width: 924px; height: 1200px; overflow: hidden; background: var(--stage); }
  .postcard {
    position: absolute; left: 104px; width: 716px; height: 471px;
    background: var(--paper);
    box-shadow: 0 6px 18px rgba(0,0,0,.25);
    overflow: hidden;
  }
  .postcard--front { top: 80px; }
  .postcard--back { top: 640px; }
  .postcard svg { display: block; width: 100%; height: 100%; }
  .headline { font-family: "Oswald", sans-serif; font-weight: 500; }
  .light { font-family: "Oswald", sans-serif; font-weight: 300; }
  .phone { font-family: "Open Sans", sans-serif; font-weight: 700; }
  .service { font-family: "Oswald", sans-serif; font-weight: 300; font-size: 14px; fill: #f2f2f2; }
  .brand { font-family: "Oswald", sans-serif; font-weight: 600; fill: var(--ink); }
  .postal { font-family: "Arimo", sans-serif; fill: #111; }
</style>
</head>
<body>

<section class="postcard postcard--front">
  <svg viewBox="0 0 875 576" xmlns="http://www.w3.org/2000/svg">
    <defs>
      <linearGradient id="houseTone" x1="0" y1="0" x2="0" y2="1">
        <stop offset="0" stop-color="#6f7a5a"/><stop offset=".55" stop-color="#5b5550"/><stop offset="1" stop-color="#74a640"/>
      </linearGradient>
      <linearGradient id="gardenTone" x1="0" y1="0" x2="0" y2="1">
        <stop offset="0" stop-color="#a8a49a"/><stop offset="1" stop-color="#6e8a3e"/>
      </linearGradient>
      <linearGradient id="shedTone" x1="0" y1="0" x2="1" y2="1">
        <stop offset="0" stop-color="#6f7d52"/><stop offset=".5" stop-color="#cbbfa5"/><stop offset="1" stop-color="#7b8e4c"/>
      </linearGradient>
      <linearGradient id="kitchenTone" x1="0" y1="0" x2="0" y2="1">
        <stop offset="0" stop-color="#e6e1d8"/><stop offset="1" stop-color="#8d8780"/>
      </linearGradient>
      <radialGradient id="panelTone" cx=".5" cy=".3" r=".9">
        <stop offset="0" stop-color="var(--charcoal-light)"/><stop offset="1" stop-color="#262628"/>
      </radialGradient>
    </defs>

    <rect class="photo-house" role="img" aria-label="Photo of a freshly painted two-storey brick house with lawn" x="0" y="0" width="470" height="268" fill="url(#houseTone)"/>
    <rect class="tile-estimates" x="0" y="268" width="157" height="118" fill="var(--charcoal)"/>
    <text class="headline" x="78" y="333" text-anchor="middle" font-size="52" fill="#fff">FREE</text>
    <text class="headline" x="78" y="371" text-anchor="middle" font-size="25" fill="#fff">ESTIMATES</text>
    <rect class="photo-garden" role="img" aria-label="Photo of a stone-edged garden bed with mulch" x="158" y="268" width="157" height="118" fill="url(#gardenTone)"/>
    <rect class="photo-shed" role="img" aria-label="Photo of a shed being pressure washed" x="316" y="268" width="174" height="238" fill="url(#shedTone)"/>
    <rect class="photo-kitchen" role="img" aria-label="Photo of a kitchen with refinished cabinets and range hood" x="0" y="387" width="157" height="119" fill="url(#kitchenTone)"/>
    <rect class="tile-licensed" x="158" y="387" width="157" height="119" fill="var(--charcoal)"/>
    <text class="light" x="236" y="426" text-anchor="middle" font-size="22" fill="#fff">FULLY</text>
    <text class="light" x="236" y="460" text-anchor="middle" font-size="32" fill="#fff">LICENSED</text>
    <text class="light" x="236" y="488" text-anchor="middle" font-size="22" fill="#fff">AND INSURED</text>

    <rect class="call-strip" x="0" y="506" width="490" height="70" fill="var(--mist)"/>
    <text class="headline" x="50" y="556" font-size="36" fill="var(--red)" textLength="176" lengthAdjust="spacingAndGlyphs">CALL US NOW!</text>
    <circle cx="253" cy="543" r="9.5" fill="none" stroke="var(--red)" stroke-width="2"/>
    <path d="M248 538c0 6 4 10 10 10l1.5-2.5-2.5-1.5-1.5 1.5c-2-1-3-2-4-4l1.5-1.5-1.5-2.5z" fill="var(--red)"/>
    <text class="phone" x="275" y="550" font-size="19" fill="var(--red)">+1 555-014-2290</text>

    <path d="M445 0H875V310H470C470 180 465 80 445 0Z" fill="var(--paper)"/>
    <path d="M430 0C455 80 462 180 462 310" fill="none" stroke="var(--red)" stroke-width="9"/>

    <path d="M490 310H875V576H462C480 500 490 420 490 310Z" fill="url(#panelTone)"/>
    <path d="M490 310C490 420 480 500 450 576" fill="none" stroke="var(--red)" stroke-width="7"/>

    <rect x="536" y="52" width="16" height="16" fill="var(--red)"/>
    <text class="brand" x="560" y="110" font-size="46" letter-spacing="1">BRINDLE</text>
    <text class="brand" x="560" y="146" font-size="34" letter-spacing="2">PAINTING</text>
    <text class="brand" x="560" y="172" font-size="17" letter-spacing="2">&amp; MAINTENANCE LLC.</text>

    <rect x="430" y="192" width="445" height="116" fill="var(--red)"/>
    <text class="headline" x="669" y="242" text-anchor="middle" font-size="21" fill="#fff" textLength="338" lengthAdjust="spacingAndGlyphs">REFRESH, RENEW &amp; REVIVE YOUR HOME.</text>
    <text class="headline" x="669" y="278" text-anchor="middle" font-size="21" fill="#fff" textLength="262" lengthAdjust="spacingAndGlyphs">FROM PAINTING TO CARPENTRY</text>
    <circle cx="442" cy="250" r="66" fill="#fff"/>
    <circle cx="442" cy="250" r="56" fill="var(--red)"/>
    <circle cx="442" cy="250" r="36" fill="none" stroke="#fff" stroke-width="2"/>

    <g class="services">
      <g fill="var(--red)">
        <circle cx="511" cy="358" r="4"/><circle cx="511" cy="384" r="4"/><circle cx="511" cy="409" r="4"/>
        <circle cx="511" cy="435" r="4"/><circle cx="511" cy="460" r="4"/>
        <circle cx="705" cy="358" r="4"/><circle cx="705" cy="384" r="4"/><circle cx="705" cy="409" r="4"/>
        <circle cx="705" cy="435" r="4"/><circle cx="705" cy="460" r="4"/>
      </g>
      <text class="service" x="522" y="363">Residential/Commercial Interior</text>
      <text class="service" x="522" y="389">Residential/Commercial Exterior</text>
      <text class="service" x="522" y="414">Trim &amp; Molding installation</text>
      <text class="service" x="522" y="440">Wainscoting</text>
      <text class="service" x="522" y="465">Wallpaper removal</text>
      <text class="service" x="716" y="363">Cabinet refinishing</text>
      <text class="service" x="716" y="389">Woodwork Enameling Deck</text>
      <text class="service" x="716" y="414">Fence Cleaning &amp; Sealing</text>
      <text class="service" x="716" y="440">Pressure wash</text>
      <text class="service" x="716" y="465">Concrete &amp; Paver Washing</text>
    </g>
    <line x1="545" y1="502" x2="825" y2="502" stroke="var(--red)" stroke-width="1"/>
    <rect x="521" y="530" width="20" height="20" fill="var(--red)"/>
    <text class="headline" x="554" y="549" font-size="20" fill="#fff" textLength="294" lengthAdjust="spacingAndGlyphs">BRINDLE PAINTING &amp; MAINTENANCE LLC</text>
  </svg>
</section>

<section class="postcard postcard--back">
  <svg viewBox="0 0 875 576" xmlns="http://www.w3.org/2000/svg">
    <defs>
      <linearGradient id="barnTone" x1="0" y1="0" x2="0" y2="1">
        <stop offset="0" stop-color="#8a3a36"/><stop offset=".6" stop-color="#7a2f2c"/><stop offset="1" stop-color="#3f5a2a"/>
      </linearGradient>
      <linearGradient id="deckTone" x1="0" y1="0" x2="1" y2="0">
        <stop offset="0" stop-color="#b49b84"/><stop offset=".55" stop-color="#a4362d"/><stop offset="1" stop-color="#8e2d25"/>
      </linearGradient>
      <linearGradient id="fenceTone" x1="0" y1="0" x2="0" y2="1">
        <stop offset="0" stop-color="#d5cdbf"/><stop offset=".7" stop-color="#b8ad9a"/><stop offset="1" stop-color="#6f9a3e"/>
      </linearGradient>
      <radialGradient id="panelTone2" cx=".5" cy=".4" r=".9">
        <stop offset="0" stop-color="var(--charcoal-light)"/><stop offset="1" stop-color="#262628"/>
      </radialGradient>
    </defs>

    <rect class="photo-barn" role="img" aria-label="Photo of a red-sided house with cream trim and ladders during painting" x="0" y="0" width="875" height="260" fill="url(#barnTone)"/>
    <path d="M0 240C200 200 420 205 560 255C700 300 800 240 875 180V576H0Z" fill="var(--paper)"/>
    <path d="M0 240C200 200 420 205 560 255C700 300 800 240 875 180" fill="none" stroke="var(--red)" stroke-width="8"/>

    <path d="M0 252C180 218 330 220 405 236C430 330 440 470 410 576H0Z" fill="url(#panelTone2)"/>
    <path d="M405 236C430 330 440 470 410 576" fill="none" stroke="var(--red)" stroke-width="8"/>
    <text class="headline" x="200" y="302" text-anchor="middle" font-size="21" fill="#fff" textLength="338" lengthAdjust="spacingAndGlyphs">REFRESH, RENEW &amp; REVIVE YOUR HOME.</text>
    <text class="headline" x="200" y="338" text-anchor="middle" font-size="21" fill="#fff" textLength="262" lengthAdjust="spacingAndGlyphs">FROM PAINTING TO CARPENTRY</text>
    <rect x="0" y="365" width="452" height="60" fill="var(--red)"/>
    <text class="light" x="202" y="403" text-anchor="middle" font-size="21" fill="#fff">PROMPT PROFESSIONAL SERVICE</text>
    <text class="headline" x="37" y="480" font-size="33" fill="#fff" textLength="152" lengthAdjust="spacingAndGlyphs">CALL US NOW!</text>
    <circle cx="213" cy="469" r="9.5" fill="none" stroke="#fff" stroke-width="2"/>
    <path d="M208 464c0 6 4 10 10 10l1.5-2.5-2.5-1.5-1.5 1.5c-2-1-3-2-4-4l1.5-1.5-1.5-2.5z" fill="#fff"/>
    <text class="phone" x="232" y="476" font-size="18" fill="#fff">+1 555-014-2290</text>
    <line x1="160" y1="495" x2="345" y2="495" stroke="var(--red)" stroke-width="1"/>
    <rect x="43" y="522" width="20" height="20" fill="var(--red)"/>
    <text class="headline" x="76" y="541" font-size="19" fill="#fff" textLength="294" lengthAdjust="spacingAndGlyphs">BRINDLE PAINTING &amp; MAINTENANCE LLC</text>

    <circle cx="609" cy="262" r="68" fill="#fff"/>
    <circle class="photo-deck" role="img" aria-label="Close-up photo of deck boards half stained red" cx="609" cy="262" r="63" fill="url(#deckTone)"/>
    <circle cx="778" cy="250" r="92" fill="#fff"/>
    <circle class="photo-fence" role="img" aria-label="Photo of a cleaned wooden privacy fence on a lawn" cx="778" cy="250" r="86" fill="url(#fenceTone)"/>

    <rect x="484" y="342" width="12" height="12" fill="var(--red)"/>
    <text class="brand" x="484" y="388" font-size="33" letter-spacing="1">BRINDLE</text>
    <text class="brand" x="484" y="414" font-size="24" letter-spacing="2">PAINTING</text>
    <text class="brand" x="484" y="432" font-size="12" letter-spacing="1.5">&amp; MAINTENANCE LLC.</text>

    <rect x="773" y="355" width="77" height="77" fill="#fff" stroke="#222" stroke-width="1"/>
    <text class="postal" font-size="10.5" text-anchor="middle">
      <tspan x="811.5" y="373">PRSRT STD</tspan>
      <tspan x="811.5" y="385">ECRWSS</tspan>
      <tspan x="811.5" y="398">U.S. Postage</tspan>
      <tspan x="811.5" y="410" font-weight="700">PAID</tspan>
      <tspan x="811.5" y="423">EDDM RETAIL</tspan>
    </text>
    <rect x="641" y="465" width="209" height="83" fill="#fff" stroke="#222" stroke-width="1"/>
    <text class="postal" x="833" y="485" text-anchor="end" font-size="8.5">******************ECRWSS****</text>
    <text class="postal" x="656" y="517" font-size="12.5">Local</text>
    <text class="postal" x="656" y="530" font-size="12.5">Postal Customer</text>
  </svg>
</section>

</body>
</html>
```